Wedding Vow Design for Modern Print - SUBWAY PRINT STYLE or Similar, MODERN

I recently got married and I want to take the main words from my wedding vows and create a design using them that I can have printed and present to my new wife. I told her that I had privileges with Marring her and I made her promises. I would like to highlight both. We have a modern home and I want something that we can have professionally framed and hung on the wall. Love modern and clean design but something interesting.

Target Market(s)

Myself. 35, modern and loves clean design.

Industry/Entity Type

Wedding

Font styles to use
Serif

Colors
f6f3f8
ffffff
fbd4d5
000000
9d9d9d
dddddd

Requirements
Must have
• Cool, clean and modern design. Neutral Colors, Clean lines, Black and White, no reds, pinks, etc.
• We will hang this in our California modern home.
Nice to have
• Our wedding colors were , Gray,Black, Light Pink. I love the Subway signs and also love Black and White Word art.
Should not have
• Flowers, squiggly lines, traditional design. Something that would look great in a stainless metal frame or mirrored frame on white walls.

```html
<!DOCTYPE html>
<html lang="en">
<head>
<meta charset="utf-8">
<title>Vows – Blessings and Pledges</title>
<link rel="stylesheet" href="https://fonts.googleapis.com/css2?family=Jost:wght@500&display=swap">
<style>
  :root {
    --paper: #ffffff;
    --ink: #000000;
  }
  html, body {
    margin: 0;
    padding: 0;
    width: 848px;
    height: 1200px;
    overflow: hidden;
    background: var(--paper);
  }
  .vow-print {
    display: block;
    width: 848px;
    height: 1200px;
  }
  .vow-print .edge-rule {
    fill: var(--ink);
  }
  .vow-print text {
    font-family: "Jost", "Futura", "Century Gothic", sans-serif;
    font-weight: 500;
    fill: var(--ink);
  }
</style>
</head>
<body>
<svg class="vow-print" viewBox="0 0 848 1200" width="848" height="1200" role="img" aria-label="Word art of wedding vows: blessings and pledges">
  <rect class="edge-rule" x="0" y="0" width="3" height="1200"/>

  <!-- Blessings -->
  <text class="word word--headline" x="18" y="100" font-size="103" textLength="530" lengthAdjust="spacingAndGlyphs">BLESSINGS</text>
  <text class="word word--small" x="570" y="62" font-size="46" textLength="252" lengthAdjust="spacing">ALL OF</text>
  <text class="word word--small" x="570" y="110" font-size="46" textLength="252" lengthAdjust="spacing">MY DAYS</text>

  <text class="word word--list" x="18" y="195" font-size="39" textLength="526" lengthAdjust="spacing">KINDNESS&#160;&#160;&#160;&#160;&#160;TRUST</text>
  <text class="word word--list" x="18" y="255" font-size="42" textLength="530" lengthAdjust="spacingAndGlyphs">DEVOTION HONESTY</text>
  <text class="word word--headline" x="562" y="252" font-size="117" textLength="260" lengthAdjust="spacingAndGlyphs">HOPE</text>

  <text class="word word--line" x="18" y="385" font-size="96" textLength="804" lengthAdjust="spacingAndGlyphs">LOYAL – FOREVER</text>

  <text class="word word--hero" x="18" y="565" font-size="179" textLength="804" lengthAdjust="spacingAndGlyphs">TOGETHER</text>

  <!-- Pledges -->
  <text class="word word--headline" x="18" y="700" font-size="117" textLength="527" lengthAdjust="spacingAndGlyphs">PLEDGES</text>
  <text class="word word--small" x="565" y="672" font-size="50" textLength="60" lengthAdjust="spacingAndGlyphs">TO</text>
  <text class="word word--small" x="680" y="672" font-size="50" textLength="142" lengthAdjust="spacingAndGlyphs">THE</text>
  <text class="word word--small" x="690" y="720" font-size="46" textLength="125" lengthAdjust="spacingAndGlyphs">END</text>

  <text class="word word--list" x="22" y="815" font-size="43" textLength="526" lengthAdjust="spacingAndGlyphs">WHOLEHEARTED RESPECT</text>
  <text class="word word--list" x="62" y="860" font-size="43" textLength="440" lengthAdjust="spacingAndGlyphs">LAUGH GROW FORGIVE</text>
  <text class="word word--headline" x="565" y="860" font-size="115" textLength="257" lengthAdjust="spacingAndGlyphs">Share</text>

  <text class="word word--line" x="18" y="1010" font-size="121" textLength="804" lengthAdjust="spacingAndGlyphs">ALL THAT YOU ARE</text>
  <text class="word word--line" x="18" y="1165" font-size="129" textLength="806" lengthAdjust="spacingAndGlyphs">ALL THAT I AM</text>
</svg>
</body>
</html>
```